Flyer for photo scanning business

Hello,
I need a flyer created for my business that would be suitable for print, to drop in letterboxes in my local community.

I would like the flyer to convey very simply the services I offer which is scanning negatives, slides and VHS tapes to digital files.
Hopefully it can make it look like an easy process, as people are often daunted by the task of sorting through old photos so they don't always get around to having them scanned.

I have a pinned facebook post that can be used by the designer to reference my services. Pricing does not need to be included on the flyer.
http://facebook.com/brightvaleimaging

Target Market(s)

Parents & Grandparents

Requirements
Must have
• Must make my services look simple! Refer to pinned facebook post for detailed outline of my services.

I would like to flyer to point towards my contact details -
www.brightvale.com
Margot 0478 219 836

Colours in line with my logo/brand (uploaded to brief).
Nice to have
• Stock images of 35mm film negatives, 8mm film, VHS tapes, or Lumavert slides would be worth including. I have also uploaded a mockup of the USB sticks that I provide with digitised images.
Should not have
• no prices needed,

```html
<!DOCTYPE html>
<html lang="en">
<head>
<meta charset="utf-8">
<title>Brightvale Imaging – Flyer</title>
<link rel="stylesheet" href="https://fonts.googleapis.com/css2?family=Work+Sans:wght@400;600;700&family=Montserrat:wght@400;700&display=swap">
<style>
  :root {
    --blue-deep: #2f6ca6;
    --blue-mid: #4a8cc6;
    --blue-light: #6fb0e0;
    --ink: #245c94;
    --heading-blue: #1f5e9c;
    --white: #ffffff;
    --paper: #ffffff;
  }
  * { margin: 0; padding: 0; box-sizing: border-box; }
  html, body { width: 1000px; height: 1200px; overflow: hidden; background: var(--paper); }
  body { font-family: "Montserrat", "Work Sans", sans-serif; position: relative; }

  .flyer { position: relative; width: 1000px; height: 1200px; }

  .panel {
    position: absolute; left: 69px; top: 0; width: 862px; height: 1085px;
    background:
      radial-gradient(ellipse 420px 260px at 50% 640px, var(--blue-light) 0%, rgba(111,176,224,0) 100%),
      radial-gradient(ellipse 300px 200px at 50% 990px, #7fc0ea 0%, rgba(127,192,234,0) 100%),
      linear-gradient(180deg, var(--blue-deep) 0%, var(--blue-mid) 45%, var(--blue-mid) 65%, var(--blue-deep) 100%);
  }

  .brand-box {
    position: absolute; left: 372px; top: 0; width: 257px; height: 155px;
    background: var(--white);
    display: flex; align-items: center; justify-content: center; gap: 10px;
  }
  .brand-dot { width: 14px; height: 14px; border-radius: 50%; background: var(--blue-mid); }
  .brand-name {
    font-family: "Montserrat", sans-serif; font-weight: 400; font-size: 19px;
    letter-spacing: 2px; color: var(--ink); text-transform: uppercase;
  }

  .headline {
    position: absolute; left: 69px; width: 862px; top: 190px;
    text-align: center; color: var(--white);
    font-family: "Work Sans", sans-serif; font-weight: 700;
    font-size: 50px; line-height: 52px;
  }
  .intro {
    position: absolute; left: 69px; width: 862px; top: 296px;
    text-align: center; color: var(--white);
    font-family: "Montserrat", sans-serif; font-weight: 400;
    font-size: 18px; line-height: 25px;
  }

  .media-strip { position: absolute; top: 396px; height: 237px; }
  .media-vhs { left: 69px; width: 287px; background: linear-gradient(135deg, #b9834f 0%, #e9e2d2 45%, #2b2b2b 80%, #c28a55 100%); }
  .media-film { left: 365px; width: 271px; background: radial-gradient(circle at 55% 30%, #8c8a86 0%, #3a3d44 40%, #15161b 100%); }
  .media-slides { left: 645px; width: 286px; background: linear-gradient(135deg, #f2d230 0%, #e24a3a 35%, #5fb4e0 65%, #1c2230 100%); }

  .steps-card {
    position: absolute; left: 118px; top: 672px; width: 764px; height: 243px;
    background: var(--white); padding: 12px 25px 0 25px; color: var(--ink);
    font-family: "Montserrat", sans-serif; font-size: 15.5px; line-height: 21px;
  }
  .steps-title {
    text-align: center; font-family: "Work Sans", sans-serif; font-weight: 700;
    font-size: 24px; color: var(--heading-blue); letter-spacing: 0.3px; margin-bottom: 2px;
  }
  .step { margin-bottom: 16px; }
  .step-label { font-family: "Work Sans", sans-serif; font-weight: 700; font-size: 17px; color: var(--heading-blue); }
  .step strong { font-weight: 700; }

  .usb-mockup {
    position: absolute; left: 388px; top: 890px; width: 230px; height: 190px;
    background: radial-gradient(ellipse at 50% 50%, #cfe4f4 0%, #8bb3d6 40%, rgba(111,160,205,0) 72%);
  }

  .feature {
    position: absolute; top: 957px; width: 260px; text-align: center;
    color: var(--white); font-family: "Work Sans", sans-serif; font-weight: 700;
    font-size: 16.5px; line-height: 21px;
  }
  .feature-photos { left: 118px; }
  .feature-video { left: 610px; width: 270px; }

  .contact {
    position: absolute; left: 0; width: 1000px; top: 1098px;
    display: flex; flex-direction: column; align-items: center;
    color: var(--ink); font-family: "Montserrat", sans-serif; font-weight: 400;
    font-size: 33px; line-height: 42px;
  }
  .contact-line { display: flex; align-items: center; gap: 12px; }
  .contact-icon { width: 26px; height: 26px; }
</style>
</head>
<body>
<main class="flyer">
  <div class="panel"></div>

  <div class="brand-box">
    <span class="brand-dot"></span>
    <span class="brand-name">Brightvale Imaging</span>
  </div>

  <h1 class="headline">Bring your precious<br>memories back to life</h1>
  <p class="intro">Brightvale Imaging is a small business run from my home in the<br>Perth Hills. I digitise photos that haven’t been seen in years,<br>bringing them back to life.</p>

  <div class="media-strip media-vhs" role="img" aria-label="Stock photo of old VHS tapes and cases on a wooden table"></div>
  <div class="media-strip media-film" role="img" aria-label="Stock photo of a pile of 35mm film canisters"></div>
  <div class="media-strip media-slides" role="img" aria-label="Stock photo of colourful plastic slide mounts"></div>

  <section class="steps-card">
    <h2 class="steps-title">JUST 3 EASY STEPS</h2>
    <p class="step"><span class="step-label">STEP 1 :</span> Find your old negatives or tapes and organise them as much or as little as you want.</p>
    <p class="step"><span class="step-label">STEP 2 :</span> Contact me here or email <strong>margot@brightvale.com</strong> and I will come and collect these from your home in the hills area.</p>
    <p class="step"><span class="step-label">STEP 3 :</span> Once completed (usually within a few days) I will drop back your box of memories with a USB stick containing high resolution JPEG files. Contactless payment will be processed when I arrive.</p>
  </section>

  <div class="usb-mockup" role="img" aria-label="Product image of the branded blue USB stick supplied with digitised files"></div>

  <p class="feature feature-photos">JPEG files are supplied at 2400 dpi which means you can easily print or enlarge your photos. They also look great on a 4k screen!</p>
  <p class="feature feature-video">VHS tapes are upscaled and captured at HD 1080p in a 100% digital workflow ensuring the best possibly quality and playback on your computer.</p>

  <footer class="contact">
    <div class="contact-line">
      <svg class="contact-icon" viewBox="0 0 26 26" aria-hidden="true">
        <rect x="1" y="1" width="24" height="24" rx="4" fill="none" stroke="#245c94" stroke-width="2"/>
        <circle cx="13" cy="13" r="7.5" fill="none" stroke="#245c94" stroke-width="1.6"/>
        <ellipse cx="13" cy="13" rx="3.2" ry="7.5" fill="none" stroke="#245c94" stroke-width="1.4"/>
        <line x1="5.5" y1="13" x2="20.5" y2="13" stroke="#245c94" stroke-width="1.4"/>
      </svg>
      <span>www.brightvale.com</span>
    </div>
    <div class="contact-line">
      <svg class="contact-icon" viewBox="0 0 26 26" aria-hidden="true">
        <rect x="1" y="1" width="24" height="24" rx="4" fill="none" stroke="#245c94" stroke-width="2"/>
        <path d="M9 6 L11.5 6 L12.5 9.5 L10.8 10.8 C11.6 12.8 13.2 14.4 15.2 15.2 L16.5 13.5 L20 14.5 L20 17 C20 18.5 18.5 19.5 17 19.2 C11.5 18.2 7.8 14.5 6.8 9 C6.5 7.5 7.5 6 9 6 Z" fill="none" stroke="#245c94" stroke-width="1.6" stroke-linejoin="round"/>
      </svg>
      <span>Margot 0478 219 836</span>
    </div>
  </footer>
</main>
</body>
</html>
```